Falcrest security business card

Looking for a business card for my security company

Target Market(s)

Security

Industry/Entity Type

Security

Contact Information for Business Card

Name - Gil Marston. Title - General manager - direct 314 862.4490 website www. falcrestsecurityservices.example email - gil@ falcrestsecurityservices.example

Requirements
Must have
• Logo attached

```html
<!DOCTYPE html>
<html lang="en">
<head>
<meta charset="utf-8">
<title>Falcrest Security Services — Business Card</title>
<link href="https://fonts.googleapis.com/css2?family=Montserrat:wght@500;700;800&family=Poppins:wght@400;500&display=swap" rel="stylesheet">
<style>
  :root {
    --stage: #e9ecee;
    --ink: #0b0b0b;
    --paper: #ffffff;
    --gold: #c9a04a;
    --pattern-top: #141414;
    --pattern-bottom: #050505;
    --muted: #2a2a2a;
  }
  * { margin: 0; padding: 0; box-sizing: border-box; }
  html, body { width: 1200px; height: 900px; overflow: hidden; }
  body {
    background: var(--stage);
    display: flex;
    flex-direction: column;
    align-items: center;
    justify-content: center;
    gap: 40px;
    font-family: "Poppins", sans-serif;
  }
  .card {
    position: relative;
    width: 700px;
    height: 400px;
    overflow: hidden;
    box-shadow: 0 8px 24px rgba(0,0,0,0.15);
  }

  /* Front */
  .card--front { background: var(--ink); }
  .card__pattern {
    position: absolute;
    inset: 0;
    background: linear-gradient(160deg, var(--pattern-top), var(--pattern-bottom));
  }
  .brand {
    position: absolute;
    display: flex;
    align-items: center;
    gap: 14px;
    font-family: "Montserrat", sans-serif;
    font-weight: 800;
    letter-spacing: 0.04em;
    text-transform: uppercase;
  }
  .brand__mark { display: block; }
  .card--front .brand {
    left: 50%; top: 50%;
    transform: translate(-50%, -50%);
    color: var(--gold);
    font-size: 64px;
  }
  .card--front .brand__mark { width: 26px; height: 26px; background: var(--gold); }

  /* Back */
  .card--back { background: var(--paper); color: var(--ink); }
  .card--back .brand {
    right: 56px; top: 58px;
    color: var(--ink);
    font-size: 44px;
  }
  .card--back .brand__mark { width: 18px; height: 18px; background: var(--ink); }

  .contact-block {
    position: absolute;
    left: 56px;
    bottom: 78px;
  }
  .person__name {
    font-family: "Montserrat", sans-serif;
    font-weight: 800;
    font-size: 26px;
    letter-spacing: 0.04em;
    text-transform: uppercase;
    line-height: 1;
  }
  .person__title {
    font-family: "Montserrat", sans-serif;
    font-weight: 700;
    font-size: 10.5px;
    letter-spacing: 0.12em;
    text-transform: uppercase;
    margin-top: 6px;
  }
  .contact-list {
    list-style: none;
    margin-top: 26px;
    display: flex;
    flex-direction: column;
    gap: 6px;
  }
  .contact-list li {
    display: flex;
    align-items: center;
    gap: 10px;
    font-size: 15px;
    color: var(--muted);
  }
  .contact-list li.contact--web { letter-spacing: 0.12em; }
  .contact-list svg { width: 14px; height: 14px; flex: none; }

  .card__band {
    position: absolute;
    left: 0; right: 0; bottom: 0;
    height: 22px;
    background: var(--ink);
  }
</style>
</head>
<body>

  <section class="card card--front" aria-label="Card front">
    <div class="card__pattern" role="img" aria-label="Dark repeating pattern of prowling big-cat silhouettes on black"></div>
    <div class="brand">
      <span class="brand__mark"></span>
      <span class="brand__name">Falcrest</span>
    </div>
  </section>

  <section class="card card--back" aria-label="Card back">
    <div class="brand">
      <span class="brand__mark"></span>
      <span class="brand__name">Falcrest</span>
    </div>

    <div class="contact-block">
      <p class="person__name">Gil Marston</p>
      <p class="person__title">General Manager</p>
      <ul class="contact-list">
        <li class="contact--phone">
          <svg viewBox="0 0 16 16" aria-hidden="true"><path d="M4 1.5c.6 0 1 .3 1.2.8l1 2.4c.2.5 0 1-.4 1.3l-1 .8c.7 1.6 2 2.9 3.6 3.7l.8-1c.3-.4.9-.6 1.3-.4l2.4 1c.5.2.8.7.7 1.2l-.3 2c-.1.5-.6.9-1.1.9C6.3 14.3 1.7 9.7 1.8 3.8c0-.5.4-1 .9-1.1z" fill="#0b0b0b"/></svg>
          <span>314 862.4490</span>
        </li>
        <li class="contact--email">
          <svg viewBox="0 0 16 16" aria-hidden="true"><rect x="1" y="3" width="14" height="10" fill="#0b0b0b"/><path d="M1.5 3.5 8 9l6.5-5.5" stroke="#fff" stroke-width="1.2" fill="none"/></svg>
          <span>gil@falcrestsecurityservices.example</span>
        </li>
        <li class="contact--web">
          <svg viewBox="0 0 16 16" aria-hidden="true"><circle cx="8" cy="8" r="6.5" fill="#0b0b0b"/><path d="M1.5 8h13M8 1.5c-2.5 3-2.5 10 0 13M8 1.5c2.5 3 2.5 10 0 13M2.6 4.8h10.8M2.6 11.2h10.8" stroke="#fff" stroke-width="0.8" fill="none"/></svg>
          <span>www.falcrestsecurityservices.example</span>
        </li>
      </ul>
    </div>

    <div class="card__band"></div>
  </section>

</body>
</html>
```